International wholesale business needs a business card

We need a business card.

Company Details:
Company Name and logo
Address, Phone number, Website
Employee Details:
Name, Designation, Mobile Number & Email address

Logo file is attached.

```html
<!DOCTYPE html>
<html lang="en">
<head>
<meta charset="utf-8">
<title>Veloran Trading – Business Card</title>
<link rel="stylesheet" href="https://fonts.googleapis.com/css2?family=Cinzel:wght@600;700&family=Montserrat:wght@400;500&display=swap">
<style>
  :root {
    --stage: #e6e6e6;
    --card-dark: #2e2e2f;
    --card-light: #ffffff;
    --brand-red: #c4262e;
    --silver: #cfcfd2;
    --ink: #3d3d40;
    --bar-grey: #b8bcc4;
  }
  * { box-sizing: border-box; margin: 0; padding: 0; }
  html, body { width: 1200px; height: 960px; overflow: hidden; }
  body {
    background: var(--stage);
    font-family: "Montserrat", sans-serif;
    position: relative;
  }
  .card {
    position: absolute;
    left: 250px;
    width: 700px;
    height: 400px;
    border-radius: 28px;
    overflow: hidden;
    box-shadow: 0 10px 30px rgba(0,0,0,.18);
  }
  .card--back { top: 60px; background: var(--card-dark); }
  .card--front { top: 500px; background: var(--card-light); }

  .brand {
    display: flex;
    align-items: center;
    gap: 12px;
  }
  .brand__dot {
    border-radius: 50%;
    flex: none;
  }
  .brand__name {
    font-family: "Cinzel", serif;
    font-weight: 700;
    white-space: nowrap;
  }
  .card--back .brand {
    position: absolute;
    left: 50%; top: 50%;
    transform: translate(-50%, -50%);
  }
  .card--back .brand__dot { width: 64px; height: 64px; background: var(--silver); }
  .card--back .brand__name { color: var(--silver); font-size: 46px; letter-spacing: 2px; }

  .card--front .brand {
    position: absolute;
    left: 40px; top: 78px;
  }
  .card--front .brand__dot { width: 30px; height: 30px; background: var(--brand-red); }
  .card--front .brand__name { color: var(--brand-red); font-size: 20px; letter-spacing: 1px; }

  .holder-disc {
    position: absolute;
    left: 380px; top: -140px;
    width: 460px; height: 460px;
    border-radius: 50%;
    background: var(--brand-red);
  }
  .holder {
    position: absolute;
    left: 440px; top: 120px;
    width: 260px;
    text-align: center;
    color: #fff;
  }
  .holder__name {
    font-family: "Cinzel", serif;
    font-weight: 700;
    font-size: 26px;
    letter-spacing: 1px;
    white-space: nowrap;
  }
  .holder__role { font-size: 15px; margin-top: 4px; }

  .edge-bar {
    position: absolute;
    left: 0; top: 290px;
    width: 10px; height: 110px;
    background: var(--bar-grey);
  }
  .contacts {
    position: absolute;
    left: 46px; top: 215px;
    list-style: none;
    color: var(--ink);
    font-size: 15px;
    line-height: 1.35;
  }
  .contacts li {
    display: flex;
    align-items: flex-start;
    gap: 12px;
    margin-bottom: 4px;
  }
  .contacts svg { width: 14px; height: 14px; margin-top: 3px; flex: none; fill: var(--brand-red); }
</style>
</head>
<body>

<section class="card card--back" aria-label="Card back">
  <div class="brand">
    <span class="brand__dot"></span>
    <span class="brand__name">VELORAN TRADING</span>
  </div>
</section>

<section class="card card--front" aria-label="Card front">
  <div class="holder-disc"></div>

  <div class="brand">
    <span class="brand__dot"></span>
    <span class="brand__name">VELORAN TRADING</span>
  </div>

  <div class="holder">
    <p class="holder__name">DANIEL HART</p>
    <p class="holder__role">President</p>
  </div>

  <div class="edge-bar"></div>

  <ul class="contacts">
    <li>
      <svg viewBox="0 0 24 24"><path d="M12 2a7 7 0 0 0-7 7c0 5 7 13 7 13s7-8 7-13a7 7 0 0 0-7-7zm0 9.5A2.5 2.5 0 1 1 12 6.5a2.5 2.5 0 0 1 0 5z"/></svg>
      <span>4120 Birchwood Road<br>Fairbanks, Alaska 99701</span>
    </li>
    <li>
      <svg viewBox="0 0 24 24"><path d="M6.6 10.8a15 15 0 0 0 6.6 6.6l2.2-2.2a1 1 0 0 1 1-.25 11.4 11.4 0 0 0 3.6.57 1 1 0 0 1 1 1V20a1 1 0 0 1-1 1A17 17 0 0 1 3 4a1 1 0 0 1 1-1h3.5a1 1 0 0 1 1 1c0 1.25.2 2.45.57 3.57a1 1 0 0 1-.25 1z"/></svg>
      <span>555-214-7730</span>
    </li>
    <li>
      <svg viewBox="0 0 24 24"><path d="M7 1h10a2 2 0 0 1 2 2v18a2 2 0 0 1-2 2H7a2 2 0 0 1-2-2V3a2 2 0 0 1 2-2zm0 3v14h10V4z"/></svg>
      <span>555-318-4462</span>
    </li>
    <li>
      <svg viewBox="0 0 24 24"><path d="M2 5h20v14H2zm2 2v.5l8 5 8-5V7z"/></svg>
      <span>info@veloranmail.com</span>
    </li>
    <li>
      <svg viewBox="0 0 24 24"><path d="M12 2a10 10 0 1 0 0 20 10 10 0 0 0 0-20zm0 2c1.2 1.5 2 3.6 2.2 6H9.8C10 7.6 10.8 5.5 12 4zm-2.2 8h4.4c-.2 2.4-1 4.5-2.2 6-1.2-1.5-2-3.6-2.2-6z"/></svg>
      <span>veloranmail.com</span>
    </li>
  </ul>
</section>

</body>
</html>
```